Bramwick Client Journey To Success

I need a one-page document that graphically shows the client's journey working with Bramwick from initial assessment to completed project. I want the journey to start at the "basecamp logo" and reach 4 summits (little mountain logos...) .

I'd like the imagery to convey the client starting at basecamp, and moving to each summit. Each summit, should list the subtext under each, as listed on the pdf doc i provided.

The description for the basecamp and 4 summits is attached.

I need the brochure to look like the other brochure that you did for me (attached) .

Target Market(s)

Restaurant Owners

Industry/Entity Type

Construction Management

Font styles to use
Sans Serif

Colors
EB3D1F
EC4F4E
F09395
F8D3D4
FCEDEE

Requirements
Must have
• My logo. Title: Client Journey To Success. Subtitle: The 4 Summits

```html
<!DOCTYPE html>
<html lang="en">
<head>
<meta charset="utf-8">
<title>Bramwick Development – Client Journey</title>
<link href="https://fonts.googleapis.com/css2?family=Open+Sans:wght@400;600;700;800&display=swap" rel="stylesheet">
<style>
  :root {
    --red: #e4262a;
    --red-deep: #b3151b;
    --maroon: #4a0f14;
    --ink: #111111;
    --text: #222222;
    --line: #555555;
    --paper: #ffffff;
    --mist: #f1f1f1;
  }
  * { margin: 0; padding: 0; box-sizing: border-box; }
  html, body { width: 1200px; height: 893px; overflow: hidden; background: var(--paper); }
  body { font-family: "Open Sans", Arial, sans-serif; color: var(--text); }

  .sheet {
    position: relative; width: 1200px; height: 893px;
    background: linear-gradient(160deg, var(--paper) 0%, var(--paper) 45%, var(--mist) 75%, var(--paper) 100%);
    overflow: hidden;
  }
  .journey-title {
    position: absolute; top: 150px; left: 0; width: 100%;
    text-align: center; font-weight: 800; font-size: 54px;
    letter-spacing: 4px; color: var(--ink);
  }
  .journey-map { position: absolute; left: 0; top: 0; }

  .brand { position: absolute; left: 60px; top: 352px; width: 130px; text-align: center; }
  .brand-mark { width: 86px; height: 86px; background: var(--red); margin: 0 auto 20px; }
  .brand-name { font-weight: 800; font-size: 13px; color: var(--ink); white-space: nowrap; margin-left: -20px; margin-right: -20px; }

  .stage { position: absolute; }
  .stage-title {
    font-weight: 700; font-size: 19px; line-height: 25px;
    color: var(--ink); text-align: center; white-space: nowrap;
  }
  .stage-steps { list-style: none; margin-top: 6px; }
  .stage-steps li {
    position: relative; font-size: 12.5px; line-height: 17px;
    padding-left: 10px; white-space: nowrap; color: var(--text);
  }
  .stage-steps li::before { content: "•"; position: absolute; left: 0; }

  .stage--basecamp { left: 235px; top: 336px; width: 150px; }
  .stage--summit1 { left: 377px; top: 568px; width: 240px; }
  .stage--summit2 { left: 604px; top: 318px; width: 160px; }
  .stage--summit3 { left: 740px; top: 568px; width: 262px; }
  .stage--summit4 { left: 1010px; top: 337px; width: 136px; }
  .stage--summit1 .stage-steps { margin-left: 18px; }
  .stage--summit3 .stage-steps { margin-left: 15px; }
  .stage--summit2 .stage-steps, .stage--summit4 .stage-steps { margin-top: 3px; }

  .site {
    position: absolute; top: 808px; left: 0; width: 100%;
    display: flex; justify-content: center; align-items: center; gap: 12px;
    font-weight: 700; font-size: 21px; color: var(--ink);
  }
  .footer-band {
    position: absolute; left: 0; top: 854px; width: 100%; height: 22px;
    background: linear-gradient(90deg, var(--red-deep) 0%, var(--red) 25%, var(--red-deep) 50%, var(--red) 70%, var(--maroon) 100%);
  }
</style>
</head>
<body>
<main class="sheet">
  <h1 class="journey-title">CLIENT JOURNEY</h1>

  <svg class="journey-map" width="1200" height="893" viewBox="0 0 1200 893" aria-hidden="true">
    <defs>
      <linearGradient id="hexFill" x1="0" y1="0" x2="0" y2="1">
        <stop offset="0" stop-color="#b3151b"/>
        <stop offset="1" stop-color="#ec2f2a"/>
      </linearGradient>
      <symbol id="hex" viewBox="-72 -60 144 120">
        <path d="M-34 -56 H34 Q40 -56 43 -51 L68 -5 Q71 0 68 5 L43 51 Q40 56 34 56 H-34 Q-40 56 -43 51 L-68 5 Q-71 0 -68 -5 L-43 -51 Q-40 -56 -34 -56 Z" fill="url(#hexFill)"/>
      </symbol>
      <symbol id="node" viewBox="-12 -12 24 24">
        <circle r="9" fill="#fff" stroke="#111" stroke-width="2"/>
        <circle r="4.5" fill="#111"/>
      </symbol>
    </defs>

    <path class="trail" d="M122 548 L215 548 C262 548 255 444 302 444 L330 444 C385 444 400 548 455 548 L530 548 C585 548 600 444 655 444 L715 444 C770 444 782 548 837 548 L905 548 C970 548 985 444 1045 444 L1078 444"
          fill="none" stroke="var(--line)" stroke-width="1.4"/>

    <!-- connectors -->
    <g stroke="var(--line)" stroke-width="1.4">
      <line x1="310" y1="444" x2="310" y2="492"/>
      <line x1="497" y1="500" x2="497" y2="548"/>
      <line x1="684" y1="444" x2="684" y2="492"/>
      <line x1="871" y1="500" x2="871" y2="548"/>
      <line x1="1078" y1="444" x2="1078" y2="492"/>
    </g>

    <!-- hexagons -->
    <use href="#hex" x="238" y="488" width="144" height="120"/>
    <use href="#hex" x="425" y="384" width="144" height="120"/>
    <use href="#hex" x="612" y="488" width="144" height="120"/>
    <use href="#hex" x="799" y="384" width="144" height="120"/>
    <use href="#hex" x="1006" y="488" width="144" height="120"/>

    <!-- chat icon -->
    <g fill="#fff" stroke="#fff">
      <path d="M284 530 h34 a4 4 0 0 1 4 4 v20 a4 4 0 0 1 -4 4 h-22 l-8 7 v-7 h-4 a4 4 0 0 1 -4 -4 v-20 a4 4 0 0 1 4 -4z" stroke="none"/>
      <path d="M326 542 h8 a4 4 0 0 1 4 4 v18 a4 4 0 0 1 -4 4 h-3 v6 l-7 -6 h-16 a4 4 0 0 1 -4 -4 v-2 h17 a5 5 0 0 0 5 -5z" stroke="none"/>
      <g stroke="#c01a1f" stroke-width="2"><line x1="290" y1="539" x2="314" y2="539"/><line x1="290" y1="545" x2="314" y2="545"/><line x1="290" y1="551" x2="306" y2="551"/></g>
    </g>

    <!-- hard hat and wrench icon -->
    <g fill="#fff">
      <path d="M472 448 a22 20 0 0 1 44 0 h4 v6 h-52 v-6z"/>
      <rect x="490" y="424" width="8" height="12" rx="2"/>
      <rect x="476" y="458" width="36" height="14" rx="4"/>
      <path d="M506 466 l14 -14 a6 6 0 1 1 4 4 l-14 14z"/>
    </g>

    <!-- clipboard icon -->
    <g fill="none" stroke="#fff" stroke-width="3">
      <rect x="666" y="520" width="36" height="46" rx="3"/>
      <rect x="677" y="515" width="14" height="8" rx="2" fill="#fff"/>
      <path d="M672 534 l3 3 5 -6 M672 545 l3 3 5 -6 M672 556 l3 3 5 -6" stroke-width="2"/>
      <path d="M684 534 h12 M684 545 h12 M684 556 h12" stroke-width="2"/>
    </g>

    <!-- checklist and hard hat icon -->
    <g fill="#fff">
      <rect x="840" y="424" width="24" height="34" rx="2" fill="none" stroke="#fff" stroke-width="3"/>
      <path d="M845 434 l2 2 4 -4 M845 442 l2 2 4 -4 M845 450 l2 2 4 -4" stroke="#fff" stroke-width="2" fill="none"/>
      <path d="M870 442 a16 15 0 0 1 32 0 h4 v5 h-40 v-5z"/>
      <rect x="882" y="424" width="8" height="10" rx="2"/>
      <rect x="872" y="452" width="30" height="14" rx="4"/>
    </g>

    <!-- gears icon -->
    <g fill="none" stroke="#fff">
      <circle cx="1068" cy="555" r="10" stroke-width="8" stroke-dasharray="4 3.5"/>
      <circle cx="1068" cy="555" r="8" stroke-width="4"/>
      <circle cx="1090" cy="537" r="7" stroke-width="6" stroke-dasharray="3 2.6"/>
      <circle cx="1090" cy="537" r="5" stroke-width="3"/>
    </g>

    <!-- nodes -->
    <circle cx="122" cy="548" r="9" fill="#fff" stroke="#111" stroke-width="2"/>
    <circle cx="122" cy="548" r="4.5" fill="var(--red)"/>
    <use href="#node" x="298" y="432" width="24" height="24"/>
    <use href="#node" x="485" y="536" width="24" height="24"/>
    <use href="#node" x="672" y="432" width="24" height="24"/>
    <use href="#node" x="859" y="536" width="24" height="24"/>
    <use href="#node" x="1066" y="432" width="24" height="24"/>
  </svg>

  <div class="brand">
    <div class="brand-mark"></div>
    <div class="brand-name">BRAMWICK DEVELOPMENT</div>
  </div>

  <section class="stage stage--basecamp">
    <h2 class="stage-title" style="text-align:left;margin-left:22px;">BASECAMP</h2>
    <ul class="stage-steps">
      <li>Client Assessment</li>
      <li>Determine Project Goals</li>
      <li>Proposal &amp; Fees</li>
    </ul>
  </section>

  <section class="stage stage--summit1">
    <h2 class="stage-title">SUMMIT 1<br>PRECONSTRUCTION</h2>
    <ul class="stage-steps">
      <li>Develop Project Plan</li>
      <li>Develop Risk Assessment &amp; Plan</li>
      <li>Devlope Schedule</li>
      <li>Develop Budget</li>
      <li>Develop Team</li>
      <li>GC, Sub, Consultants Contracts</li>
    </ul>
  </section>

  <section class="stage stage--summit2">
    <h2 class="stage-title">SUMMIT 2<br>EXECUTION</h2>
    <ul class="stage-steps">
      <li>Acquire Permits</li>
      <li>PreConstruction Meeting</li>
      <li>Project Start</li>
    </ul>
  </section>

  <section class="stage stage--summit3">
    <h2 class="stage-title">SUMMIT 3<br>PROJECT MANAGEMENT</h2>
    <ul class="stage-steps">
      <li>Shared Consciousness Meetings</li>
      <li>Pressurized Collaboration</li>
      <li>Schedule Management</li>
      <li>Run O.O.D.A. Loop</li>
    </ul>
  </section>

  <section class="stage stage--summit4">
    <h2 class="stage-title">SUMMIT 4<br>EXECUTION</h2>
    <ul class="stage-steps" style="margin-left:12px;">
      <li>Closeout</li>
    </ul>
  </section>

  <div class="site">
    <svg width="20" height="20" viewBox="0 0 20 20" aria-hidden="true">
      <g fill="none" stroke="#111" stroke-width="1.6">
        <circle cx="10" cy="10" r="8.5"/>
        <ellipse cx="10" cy="10" rx="3.8" ry="8.5"/>
        <line x1="1.5" y1="10" x2="18.5" y2="10"/>
        <path d="M3.5 5.5 h13 M3.5 14.5 h13"/>
      </g>
    </svg>
    <span>www.bramwickdevgroup.com</span>
  </div>

  <div class="footer-band"></div>
</main>
</body>
</html>
```